Newsletter Design Project for electrical maintenance company

1.We need a monthly newsletter tempate designed in mail chimp.
2. We will provide the basic information for the newsletter
3. you will edit and copy write newsletter
We would love this to be an on going monthly partnership
For now, design template and do 1 newsletter
Its a light hearted news letter
40% relavent info. e.g. talk about smoke alarms
Personal information about what we are up to - family etc
update on workers - whos new, perosnal profiles etc
each newsletter to have a specific product special
e.g. $50 off second smoke alarm
Each news letter to contain 5 energy saving tips
www.brightlanehelpers.com.au for more company info
residiential home owners - Mainly females
Electrical

```html
<!DOCTYPE html>
<html lang="en">
<head>
<meta charset="utf-8">
<title>Bright Lane Helpers – Monthly Newsletter</title>
<link rel="stylesheet" href="https://fonts.googleapis.com/css2?family=Arimo:wght@400;700&family=Roboto+Condensed:wght@400;700&family=Bangers&display=swap">
<style>
:root{
  --sky-top:#2f8fd8;
  --sky-mid:#8fc8ef;
  --sky-low:#e8f4fb;
  --panel:#edf5f8;
  --navy:#1b3d5c;
  --blue-band:#1e9be0;
  --brand-green:#5cbf1f;
  --leaf:#1e9b3a;
  --orange:#f06a1c;
  --red:#e31b1b;
  --text:#222;
  --muted:#555;
  --rule:#d8e2e6;
  --yellow:#f7d217;
  --mint:#8ccaa0;
}
*{box-sizing:border-box;margin:0;padding:0}
html,body{width:1200px;height:2810px;overflow:hidden}
body{background:#fff;font-family:"Arimo",Arial,sans-serif;color:var(--text);position:relative}
.abs{position:absolute}

.sky{left:0;top:0;width:1200px;height:560px;background:linear-gradient(180deg,var(--sky-top) 0%,var(--sky-mid) 45%,var(--sky-low) 80%,#fff 100%)}
.site-url{left:22px;top:12px;font-size:22px;color:#fff}
.top-links{right:40px;top:10px;display:flex;gap:40px;font-size:21px;font-weight:700;color:#fff}
.top-links span{display:flex;align-items:center;gap:12px}

.mascot{left:450px;top:70px;width:300px;height:230px;border-radius:20px;background:radial-gradient(circle,#7fbf4a 0%,#e0892b 55%,rgba(255,255,255,0) 75%)}
.brand-mark{left:0;width:1200px;top:300px;display:flex;justify-content:center;align-items:center;gap:12px;font-family:"Roboto Condensed",sans-serif;font-weight:700;font-size:30px;color:#e0761c}
.brand-mark i{width:22px;height:22px;border-radius:50%;background:#e0761c;display:block}
.title{left:0;width:1200px;top:372px;text-align:center;font-family:"Roboto Condensed",sans-serif;font-weight:700;font-size:76px;line-height:90px;color:var(--brand-green);letter-spacing:2px}

.panel{left:30px;top:470px;width:1140px;height:2340px;background:var(--panel);box-shadow:0 0 18px rgba(0,0,0,.12)}
.promo-band{left:18px;top:485px;width:1164px;height:52px;background:var(--blue-band);color:#fff;font-family:"Roboto Condensed",sans-serif;font-size:32px;font-weight:700;text-align:center;line-height:52px}

.h-section{font-family:"Roboto Condensed",sans-serif;font-weight:700;font-size:50px}
.about-h{left:50px;top:560px;color:var(--navy)}
.about-rule{left:50px;top:626px;width:640px;height:2px;background:var(--rule)}
.about-copy{left:55px;top:650px;width:650px;font-size:21px;line-height:32px;color:var(--text)}
.about-copy p{margin-bottom:32px}

.photo-frame{left:782px;top:608px;width:342px;height:370px;background:#fff;border:2px solid #ccd;padding:14px}
.photo{width:100%;height:320px;background:linear-gradient(160deg,#6f86a0 0%,#2f58a8 60%,#1d2f6a 100%)}
.name-ribbon{left:760px;top:955px;width:386px;height:65px;background:var(--red);border-radius:6px;color:#fff;font-family:"Roboto Condensed",sans-serif;font-weight:700;font-size:30px;text-align:center;line-height:65px}

.mail-btn{left:50px;top:1068px;width:200px;height:68px;border-radius:34px;background:linear-gradient(#b5ec3f,#62b81c);color:#1e3a0e;font-family:"Roboto Condensed",sans-serif;font-size:31px;text-align:center;line-height:68px;box-shadow:0 3px 5px rgba(0,0,0,.25)}
.call-line{left:272px;top:1066px;display:flex;align-items:baseline;gap:16px;font-family:"Roboto Condensed",sans-serif;font-weight:700}
.call-line small{font-size:32px;color:var(--text)}
.call-line strong{font-size:52px;color:var(--red)}

.promise-h{left:52px;top:1248px;color:var(--orange)}
.tips-h{left:565px;top:1248px;color:var(--leaf)}
.promise-rule{left:52px;top:1312px;width:300px;height:2px;background:var(--rule)}
.tips-rule{left:565px;top:1312px;width:540px;height:2px;background:var(--rule)}
.checklist{list-style:none;font-size:21px}
.checklist li{display:flex;align-items:center;gap:20px;height:55px}
.promise-list{left:62px;top:1340px}
.tips-list{left:575px;top:1340px}

.offer-h{left:0;width:1200px;top:1660px;display:flex;align-items:center;justify-content:center;gap:26px;color:var(--red);font-family:"Roboto Condensed",sans-serif;font-weight:700;font-size:48px}
.offer-h::before,.offer-h::after{content:"";width:290px;height:6px;border-top:2px solid #f29a5a;border-bottom:2px solid #f29a5a}

.coupons{left:50px;top:1740px;width:1098px;height:540px;background:#111;display:flex;gap:6px;padding:6px}
.coupon{flex:1;background:var(--yellow);padding:8px;display:flex;flex-direction:column;gap:8px;font-family:"Bangers",cursive;letter-spacing:1px}
.burst{height:228px;display:flex;flex-direction:column;align-items:center;justify-content:center;color:var(--red);font-size:86px;line-height:.85}
.burst-yellow{background:radial-gradient(circle,#fff7b0,#f5cd12)}
.burst-blue{background:radial-gradient(circle,#ffffff,#3f4fa7)}
.burst-black{background:radial-gradient(circle,#ffffff,#222)}
.code-box,.save-box{background:#fff;border:2px solid #111;height:112px;position:relative}
.tab{position:absolute;left:0;top:0;background:var(--mint);border:2px solid #111;border-left:0;border-top:0;font-size:28px;padding:2px 14px;color:#111}
.code-box p{position:absolute;left:0;right:0;top:58px;text-align:center;font-size:25px;color:#111}
.save-box .save{position:absolute;right:24px;top:0;font-size:44px;color:var(--red)}
.save-box p{position:absolute;left:0;right:0;top:58px;text-align:center;font-size:22px;line-height:24px;color:#1d3aa6}
.expiry{font-size:20px;text-align:right;padding-right:14px;color:#111}

.social-box{left:62px;top:2330px;width:622px;height:188px;background:#fff;border:2px solid #d3d3d3;border-radius:20px;box-shadow:0 2px 6px rgba(0,0,0,.12)}
.find-tag{left:50px;top:2375px;width:110px;height:40px;background:var(--red);color:#fff;font-family:"Roboto Condensed",sans-serif;font-weight:700;font-size:24px;line-height:40px;text-align:center;transform:rotate(-45deg)}
.social-row{left:150px;top:2362px;display:flex;gap:44px}
.social{display:flex;flex-direction:column;align-items:center;gap:8px;font-size:18px;color:var(--muted)}
.social i{width:98px;height:98px;border-radius:50%;background:radial-gradient(circle at 40% 35%,#6fb6e6,#1d5f9c);display:block}

.call-now{left:720px;top:2336px;font-family:"Roboto Condensed",sans-serif;font-weight:700;font-size:40px;color:#111}
.call-number{left:720px;top:2392px;display:flex;align-items:center;gap:16px;font-family:"Roboto Condensed",sans-serif;font-size:48px;color:var(--red)}
.call-number i{width:76px;height:76px;border-radius:50%;background:#2ea4e6;display:block}

.unsubscribe{left:84px;top:2538px;font-size:24px;color:var(--text)}
.unsubscribe a{color:#1e7cc0;text-decoration:underline}
.footer-rule{left:110px;top:2606px;width:980px;height:2px;background:var(--rule)}
.footer{left:0;width:1200px;top:2644px;text-align:center;font-size:21px;color:var(--text)}
</style>
</head>
<body>
<div class="abs sky"></div>
<div class="abs site-url">http://www.brightlanehelpers.com.au</div>
<div class="abs top-links">
  <span><svg width="22" height="24" viewBox="0 0 22 24"><circle cx="11" cy="7" r="6" fill="#fff"/><path d="M0 24c0-7 5-10 11-10s11 3 11 10z" fill="#fff"/></svg>Forward to your friends</span>
  <span><svg width="28" height="20" viewBox="0 0 28 20"><rect width="28" height="20" fill="#fff"/><path d="M0 0l14 11L28 0" stroke="#2f8fd8" stroke-width="2" fill="none"/></svg>Online Versions</span>
</div>

<div class="abs mascot" role="img" aria-label="Cartoon superhero electrician mascot holding a light bulb"></div>
<div class="abs brand-mark"><i></i>Bright Lane Helpers</div>
<div class="abs title">BRIGHT LANE HELPERS</div>

<div class="abs panel"></div>
<div class="abs promo-band">$50% OFF SECOND SMOKE ALARM, HURRY , OFER VALIDS TILL 23RD JULY, 2013</div>

<h1 class="abs h-section about-h">ABOUT DANIEL</h1>
<div class="abs about-rule"></div>
<div class="abs about-copy">
  <p>My name is Daniel Hart licensed master electrician, founder and CEO of Bright Lane Helpers.</p>
  <p>My mission at Bright Lane Helpers is to provide our customers with prompt, efficient, reliable, high quality electrical repair and installation services where we are recognised as the undisputed leaders in service excellence &amp; workmanship.</p>
  <p>My aim is for each and every customer to grow and build a healthy relationship with Bright Lane Helpers for life.</p>
  <p>Why not try us out and see for yourself.</p>
</div>
<div class="abs photo-frame"><div class="photo" role="img" aria-label="Portrait photo of the founder in a blue work shirt"></div></div>
<div class="abs name-ribbon">DANIEL HART</div>

<div class="abs mail-btn">MAIL ME</div>
<div class="abs call-line"><small>or call</small><strong>1300 555 214</strong></div>

<h2 class="abs h-section promise-h">OUR PROMISE</h2>
<div class="abs promise-rule"></div>
<ul class="abs checklist promise-list">
  <li><svg width="26" height="24" viewBox="0 0 26 24"><path d="M2 13l8 8L24 3" stroke="#e31b1b" stroke-width="6" fill="none"/></svg>On time guarantee</li>
  <li><svg width="26" height="24" viewBox="0 0 26 24"><path d="M2 13l8 8L24 3" stroke="#e31b1b" stroke-width="6" fill="none"/></svg>Up front pricing</li>
  <li><svg width="26" height="24" viewBox="0 0 26 24"><path d="M2 13l8 8L24 3" stroke="#e31b1b" stroke-width="6" fill="none"/></svg>No mess guarantee</li>
  <li><svg width="26" height="24" viewBox="0 0 26 24"><path d="M2 13l8 8L24 3" stroke="#e31b1b" stroke-width="6" fill="none"/></svg>12 month warranty</li>
  <li><svg width="26" height="24" viewBox="0 0 26 24"><path d="M2 13l8 8L24 3" stroke="#e31b1b" stroke-width="6" fill="none"/></svg>Quality service</li>
</ul>

<h2 class="abs h-section tips-h">5 ENERGY SAVING TIPS</h2>
<div class="abs tips-rule"></div>
<ul class="abs checklist tips-list">
  <li><svg width="26" height="24" viewBox="0 0 26 24"><path d="M2 13l8 8L24 3" stroke="#e31b1b" stroke-width="6" fill="none"/></svg>In luctus justo sed magna porttitor,elit vehicula.</li>
  <li><svg width="26" height="24" viewBox="0 0 26 24"><path d="M2 13l8 8L24 3" stroke="#e31b1b" stroke-width="6" fill="none"/></svg>Cras luctus sem at mi fermentum, in aliquam .</li>
  <li><svg width="26" height="24" viewBox="0 0 26 24"><path d="M2 13l8 8L24 3" stroke="#e31b1b" stroke-width="6" fill="none"/></svg>Suspena, tristique urna a, porttitor sapien.</li>
  <li><svg width="26" height="24" viewBox="0 0 26 24"><path d="M2 13l8 8L24 3" stroke="#e31b1b" stroke-width="6" fill="none"/></svg>Suspendisse non smalesuada vel ac eros.</li>
  <li><svg width="26" height="24" viewBox="0 0 26 24"><path d="M2 13l8 8L24 3" stroke="#e31b1b" stroke-width="6" fill="none"/></svg>Suspena, tristique urna a, porttitor sapien.</li>
</ul>

<h2 class="abs offer-h">CURRENT SPECIAL OFFER</h2>

<div class="abs coupons">
  <div class="coupon">
    <div class="burst burst-yellow" role="img" aria-label="Yellow sunburst behind the saving amount"><span>SAVE</span><span>$50</span></div>
    <div class="code-box"><span class="tab">...QUOTE...</span><p>“ALARM50” WHEN YOU CALL</p></div>
    <div class="save-box"><span class="tab">...AND...</span><span class="save">SAVE</span><p>SMOKE ALARM INSTALLATIONS</p></div>
    <div class="expiry">* OFFER EXPIRES 30/06/2011</div>
  </div>
  <div class="coupon">
    <div class="burst burst-blue" role="img" aria-label="Blue sunburst behind the saving amount"><span>SAVE</span><span>$50</span></div>
    <div class="code-box"><span class="tab">...QUOTE...</span><p>“WEB50” WHEN YOU CALL ...</p></div>
    <div class="save-box"><span class="tab">...AND...</span><span class="save">SAVE</span><p>BATHROOM LIGHT/ FAN/ HEAT<br>COMBO INSTALLATIONS</p></div>
    <div class="expiry">* OFFER EXPIRES 30/06/2011</div>
  </div>
  <div class="coupon">
    <div class="burst burst-black" role="img" aria-label="Black sunburst behind the saving amount"><span>SAVE</span><span>$40</span></div>
    <div class="code-box"><span class="tab">...QUOTE...</span><p>“CEILING40” WHEN YOU CALL</p></div>
    <div class="save-box"><span class="tab">...AND...</span><span class="save">SAVE</span><p>CEILING FAN INSTALLATIONS</p></div>
    <div class="expiry">* OFFER EXPIRES 30/06/2011</div>
  </div>
</div>

<div class="abs social-box"></div>
<div class="abs find-tag">FIND US</div>
<div class="abs social-row">
  <div class="social"><i></i>Pageboard</div>
  <div class="social"><i></i>Shortnote</div>
  <div class="social"><i></i>Workweb</div>
  <div class="social"><i></i>Reelhub</div>
</div>

<div class="abs call-now">CALL NOW</div>
<div class="abs call-number"><i></i>1300 555 214</div>

<div class="abs unsubscribe">Unsubscribe Us? <a href="#">Click Here</a></div>
<div class="abs footer-rule"></div>
<div class="abs footer">Marrickvale, Sydney, Australia NSW 2299, ABN: 00 111 222 333, Lic no: 400512K</div>
</body>
</html>
```